Your Road Counsel Billboard Design for Personal Injury Law Firm

Need a billboard design that we can use for different versions. 1400px X 400px jpeg or png
I have attached the logo and the attorney for the billboard. Attorney Dana Whitfield
Here is a link to our current website yourroadcounsel-example.com

HEADLINE: HIT BY A TRUCK?
SUBHEAD: NO FEE. BIG FIGHT.
855-MARGOT-7

HEADLINE: ACCIDENT?
SUBHEAD: NO FEE, UNLESS WE WIN!
855-MARGOT-7

HEADLINE: BIG TRUCK. BIG CASE.
SUBHEAD: YOU PAY $0 UPFRONT
855-MARGOT-7

Target Market(s)

People in Car Accident

Industry/Entity Type

Personal Injury Attorneys

```html
<!DOCTYPE html>
<html lang="en">
<head>
<meta charset="UTF-8">
<title>Your Road Counsel – Hit By A Truck Billboard</title>
<link rel="stylesheet" href="https://fonts.googleapis.com/css2?family=Poppins:wght@500;600;800&display=swap">
<style>
  :root {
    --bg-deep: #060b10;
    --bg-mid: #0b151b;
    --green: #5ad43f;
    --green-dark: #1d4a1e;
    --cream: #fbf6ea;
    --phone-tint: #e2f7d2;
    --photo-sky: #c9cfcf;
    --photo-road: #5b5d60;
  }
  * { margin: 0; padding: 0; box-sizing: border-box; }
  html, body {
    width: 1200px;
    height: 343px;
    overflow: hidden;
    background: var(--bg-deep);
  }
  .billboard {
    position: relative;
    width: 1200px;
    height: 343px;
    overflow: hidden;
    background:
      radial-gradient(ellipse 380px 220px at 470px 300px, rgba(70, 160, 60, 0.35), transparent 70%),
      linear-gradient(90deg, var(--bg-mid) 0%, var(--bg-deep) 60%);
    font-family: "Poppins", sans-serif;
  }
  .scene-art {
    position: absolute;
    inset: 0;
    width: 1200px;
    height: 343px;
  }
  .message {
    position: absolute;
    left: 485px;
    width: 680px;
    top: 0;
    height: 343px;
    text-align: center;
    white-space: nowrap;
  }
  .brand {
    position: absolute;
    top: 54px;
    left: 52px;
    display: flex;
    align-items: center;
    gap: 10px;
    color: var(--cream);
    font-weight: 600;
    font-size: 19px;
    line-height: 1;
    letter-spacing: 1.5px;
    text-transform: uppercase;
  }
  .brand-dot {
    width: 26px;
    height: 26px;
    border-radius: 50%;
    background: var(--green);
  }
  .headline {
    position: absolute;
    top: 110px;
    left: 0;
    width: 100%;
    color: var(--cream);
    font-weight: 800;
    font-size: 68px;
    line-height: 1;
    letter-spacing: 0.5px;
  }
  .headline .accent { color: var(--green); }
  .subhead {
    position: absolute;
    top: 184px;
    left: 0;
    width: 100%;
    color: var(--cream);
    font-weight: 500;
    font-size: 42px;
    line-height: 1;
    letter-spacing: 6px;
  }
  .phone {
    position: absolute;
    top: 252px;
    left: 0;
    width: 100%;
    color: var(--phone-tint);
    font-weight: 600;
    font-size: 52px;
    line-height: 1;
    letter-spacing: 0.5px;
    text-shadow: 0 0 14px rgba(120, 230, 90, 0.55);
  }
</style>
</head>
<body>
  <div class="billboard">
    <svg class="scene-art" viewBox="0 0 1200 343">
      <defs>
        <linearGradient id="photoTone" x1="0" y1="0" x2="0" y2="1">
          <stop offset="0" stop-color="#c9cfcf"/>
          <stop offset="0.45" stop-color="#7f8584"/>
          <stop offset="0.75" stop-color="#2c3034"/>
          <stop offset="1" stop-color="#5b5d60"/>
        </linearGradient>
        <linearGradient id="edgeFade" x1="0" y1="0" x2="1" y2="0">
          <stop offset="0" stop-color="#5ad43f"/>
          <stop offset="1" stop-color="#1d4a1e"/>
        </linearGradient>
      </defs>
      <path class="edge-band" fill="url(#edgeFade)"
        d="M0,0 H400 C395,40 440,72 515,88 C445,120 420,210 478,315 C430,300 395,320 385,343 H0 Z"/>
      <path class="photo-area" role="img" aria-label="Photo of a dark sedan crashed into the side of a semi truck on a road"
        fill="url(#photoTone)"
        d="M0,0 H385 C380,45 420,75 480,90 C420,125 400,205 448,305 C405,300 375,318 365,343 H0 Z"/>
      <path fill="#5ad43f" d="M0,0 H40 C25,15 10,30 0,50 Z"/>
      <path fill="#5ad43f" d="M160,343 C190,318 240,315 270,343 Z"/>
      <path fill="#5ad43f" d="M0,343 V320 C12,328 22,335 30,343 Z"/>
    </svg>

    <div class="message">
      <div class="brand"><span class="brand-dot"></span>Your Road Counsel</div>
      <h1 class="headline">HIT BY A <span class="accent">TRUCK?</span></h1>
      <p class="subhead">NO FEE. BIG FIGHT.</p>
      <p class="phone">855-MARGOT-7</p>
    </div>
  </div>
</body>
</html>
```